Flyer for the Harvest of lanterns conference

Flyer design for an annual international conference called "MERIVAL 2017". This is a conference for young adults, so we hope to produce a design that is both professional and appealing to young people in general

We'd like the flyer to showcase the conference brand logo, and clearly highlight the key information to people who will read it.

Target Market(s)

Young people, young adults

Industry/Entity Type

Religious

Font styles to use
Sans Serif

Colors

Designer to choose colors to be used in the design.

Requirements
Must have
• - Should be only one page (Vertical or Horizontal).
• - the MERVAL logo and all the information found in the attached text file. This includes: Main topic: Your sons and daughters shall prophesy,
• Dates and time, location, contact information and everything that is in the attached text file.
Nice to have
• It would be nice to see samples where the white logo is used and another where the black one is used.
Should not have
• This is NOT a folded flyer, we will be sticking it on doors and public places. And we will be printing large simple to put on walls. So only one page with few words like an add (the words are in the attached file)

```html
<!DOCTYPE html>
<html lang="en">
<head>
<meta charset="utf-8">
<title>MERIVAL 2017 Flyer</title>
<link href="https://fonts.googleapis.com/css2?family=Montserrat:wght@500;600;700;800&display=swap" rel="stylesheet">
<style>
  :root {
    --canvas: #e6e3df;
    --paper: #f3f3f3;
    --brown-dark: #9a4a16;
    --brown: #b8621f;
    --orange: #e2701e;
    --gold: #f2b320;
    --gold-light: #f7c948;
    --ink: #2b2b2b;
    --ink-soft: #4a4a4a;
    --white: #ffffff;
  }
  * { box-sizing: border-box; margin: 0; padding: 0; }
  html, body {
    width: 1200px; height: 1000px; overflow: hidden;
    background: var(--canvas);
    font-family: "Montserrat", Arial, sans-serif;
  }
  .flyer {
    position: absolute; left: 40px; top: 103px;
    width: 1120px; height: 794px;
    background: var(--paper);
    overflow: hidden;
    box-shadow: 0 6px 24px rgba(0,0,0,.18);
  }
  .flyer-shapes { position: absolute; inset: 0; }

  /* Left: brand and event details */
  .brand {
    position: absolute; left: 0; width: 280px; top: 52px;
    text-align: center;
  }
  .brand-mark {
    width: 140px; height: 140px; margin: 0 auto;
    border-radius: 50%; border: 4px solid var(--gold);
  }
  .brand-name {
    margin-top: 14px;
    font-weight: 800; font-size: 44px; letter-spacing: 1px;
    color: var(--ink);
  }
  .event-title {
    position: absolute; left: 53px; top: 307px; width: 357px; height: 53px;
    border: 3px solid var(--orange);
    font-weight: 700; font-size: 38px; line-height: 47px;
    color: var(--ink); text-align: center;
  }
  .event-subtitle {
    position: absolute; left: 53px; top: 366px; width: 357px;
    font-weight: 500; font-size: 21px; color: var(--ink-soft); text-align: center;
  }
  .event-when {
    position: absolute; left: 53px; top: 420px; width: 357px; text-align: center;
    color: var(--ink);
  }
  .event-month { font-weight: 800; font-size: 26px; }
  .event-dates { font-weight: 700; font-size: 19px; margin-top: 4px; }
  .event-dates sup { font-size: 11px; }
  .event-room { font-weight: 700; font-size: 19px; margin-top: 2px; }
  .event-divider {
    position: absolute; left: 100px; top: 518px; width: 263px; height: 1px;
    background: #9b9b9b;
  }
  .event-venue {
    position: absolute; left: 53px; top: 530px; width: 357px; text-align: center;
    font-weight: 600; font-size: 15px; line-height: 19px; color: var(--ink-soft);
  }
  .event-venue svg { width: 12px; height: 14px; vertical-align: -2px; margin-right: 4px; }

  /* Right: theme and speakers */
  .theme {
    position: absolute; left: 590px; width: 450px; top: 70px;
    text-align: center; color: var(--white);
    font-weight: 800; font-size: 38px; line-height: 48px;
  }
  .speakers-heading {
    position: absolute; left: 600px; width: 430px; top: 272px;
    display: flex; align-items: center; gap: 16px;
    color: var(--gold-light); font-weight: 700; font-size: 26px;
  }
  .speakers-heading::before, .speakers-heading::after {
    content: ""; flex: 1; height: 2px; background: rgba(255,255,255,.75);
  }
  .speakers {
    position: absolute; left: 560px; width: 510px; top: 324px;
    list-style: none; text-align: center;
  }
  .speaker {
    font-weight: 700; font-size: 22px; line-height: 28px; color: var(--white);
  }
  .speaker + .speaker::before {
    content: "•••"; display: block;
    font-size: 10px; line-height: 21px; letter-spacing: 2px; color: var(--white);
  }
  .speaker-title { color: var(--gold-light); }

  /* Contact */
  .contact {
    position: absolute; right: 74px; top: 665px; text-align: right;
    color: var(--ink); font-weight: 700; font-size: 20px; line-height: 33px;
  }
  .contact-label { font-size: 20px; }
  .contact svg { width: 18px; height: 18px; vertical-align: -3px; margin-right: 4px; }
  .contact .sep { margin: 0 6px; }
</style>
</head>
<body>
<main class="flyer">
  <svg class="flyer-shapes" viewBox="0 0 1120 794" width="1120" height="794">
    <defs>
      <linearGradient id="panelGrad" x1="0" y1="0" x2="1" y2="1">
        <stop offset="0" stop-color="#a9521a"/>
        <stop offset="0.55" stop-color="#c06a22"/>
        <stop offset="1" stop-color="#9a4a16"/>
      </linearGradient>
      <linearGradient id="skylineGrad" x1="0" y1="0" x2="0" y2="1">
        <stop offset="0" stop-color="#f3f3f3"/>
        <stop offset="0.5" stop-color="#dcdcdc"/>
        <stop offset="1" stop-color="#e9e9e9"/>
      </linearGradient>
      <linearGradient id="goldGrad" x1="0" y1="0" x2="1" y2="0">
        <stop offset="0" stop-color="#f5b51f"/>
        <stop offset="1" stop-color="#e29a12"/>
      </linearGradient>
    </defs>
    <rect class="skyline" x="0" y="140" width="560" height="500" fill="url(#skylineGrad)" role="img" aria-label="Faint city skyline photograph behind the event details"/>
    <polygon points="425,0 438,0 538,640 525,640" fill="var(--orange)"/>
    <polygon points="457,0 1120,0 1120,640 560,640" fill="url(#panelGrad)"/>
    <path d="M0,612 Q560,548 1120,566 L1120,584 Q560,574 0,646 Z" fill="url(#goldGrad)"/>
    <path d="M0,658 Q560,592 1120,598" fill="none" stroke="var(--orange)" stroke-width="5"/>
    <path d="M0,664 Q560,600 1120,604 L1120,794 L0,794 Z" fill="var(--white)"/>
  </svg>

  <div class="brand">
    <div class="brand-mark"></div>
    <div class="brand-name">MERVAL</div>
  </div>

  <h1 class="event-title">MERIVAL 2017</h1>
  <p class="event-subtitle">Harvest of lanterns conference</p>
  <div class="event-when">
    <p class="event-month">SEPTEMBER</p>
    <p class="event-dates">1<sup>ST</sup>, 2<sup>ND</sup> AND 3<sup>RD</sup> 2017 | 6:00PM</p>
    <p class="event-room">ROOM: WILDWOOD BALLROOM</p>
  </div>
  <div class="event-divider"></div>
  <p class="event-venue">
    <svg viewBox="0 0 12 16"><path d="M6 0C2.7 0 0 2.6 0 5.9 0 10 6 16 6 16s6-6 6-10.1C12 2.6 9.3 0 6 0zm0 8.2A2.3 2.3 0 1 1 6 3.6a2.3 2.3 0 0 1 0 4.6z" fill="#333"/></svg>Harbor Crest Inn<br>
    418 Elm Street<br>
    Bayview, ME 04000 United States
  </p>

  <h2 class="theme">YOUR SONS AND<br>DAUGHTERS<br>SHALL PROPHESY</h2>
  <h3 class="speakers-heading">SPEAKERS</h3>
  <ul class="speakers">
    <li class="speaker"><span class="speaker-title">PROPHET</span> LAURENT OBENGA</li>
    <li class="speaker"><span class="speaker-title">BISHOP</span> MARCEL TSHIBOLA</li>
    <li class="speaker"><span class="speaker-title">PROPHET</span> ANDRE LUKENI MAVU</li>
    <li class="speaker"><span class="speaker-title">PROPHET</span> PASCAL EBONDO</li>
    <li class="speaker"><span class="speaker-title">PROPHET</span> SIMON MALONGA</li>
  </ul>

  <address class="contact" style="font-style:normal">
    <div class="contact-label">Contact Info:</div>
    <div>
      <svg viewBox="0 0 20 20"><circle cx="10" cy="10" r="9" fill="none" stroke="var(--orange)" stroke-width="2"/><path d="M7 5l2 3-1.3 1.3a7 7 0 0 0 3 3L12 11l3 2-1 2c-4 0-8-4-8-8z" fill="var(--orange)"/></svg>+1 (555) 014 2290<span class="sep">|</span><svg viewBox="0 0 20 20"><rect x="2" y="4" width="16" height="12" fill="none" stroke="var(--orange)" stroke-width="2"/><path d="M2 5l8 6 8-6" fill="none" stroke="var(--orange)" stroke-width="2"/></svg>hello@lanterngate.org
    </div>
    <div>
      <svg viewBox="0 0 20 20"><circle cx="10" cy="10" r="8" fill="none" stroke="var(--orange)" stroke-width="2"/><ellipse cx="10" cy="10" rx="3.5" ry="8" fill="none" stroke="var(--orange)" stroke-width="1.5"/><path d="M2 10h16" stroke="var(--orange)" stroke-width="1.5"/></svg>www.meritvale.org
    </div>
  </address>
</main>
</body>
</html>
```